Vorapo Business Card

Need a double sided business card. Would like the business card to have the logo on one side and the employees details and business contact details on the other.

Business

```html
<!DOCTYPE html>
<html lang="en">
<head>
<meta charset="utf-8">
<title>Vorapo Business Card</title>
<link rel="stylesheet" href="https://fonts.googleapis.com/css2?family=Open+Sans:wght@400;600;700&display=swap">
<style>
  :root {
    --stage: #e6e2da;
    --slate: #7e8a92;
    --slate-dark: #6f7a82;
    --lime: #8dc63f;
    --lime-faint: #eef5e2;
    --ink: #1d1d1d;
    --muted: #8f9499;
    --paper: #ffffff;
  }
  * { box-sizing: border-box; margin: 0; padding: 0; }
  html, body {
    width: 1200px; height: 1023px; overflow: hidden;
    background: var(--stage);
    font-family: "Open Sans", sans-serif;
  }
  .sheet { position: relative; width: 1200px; height: 1023px; }
  .card {
    position: absolute; left: 250px; width: 700px; height: 400px;
    box-shadow: 0 6px 18px rgba(0,0,0,.15);
    overflow: hidden;
  }
  /* Front side */
  .card--front { top: 70px; background: var(--slate); }
  .card--front .brand {
    position: absolute; left: 0; right: 0; top: 140px;
    text-align: center; font-weight: 700; font-size: 84px;
    color: var(--lime); letter-spacing: -1px; line-height: 1;
  }
  .card--front .site {
    position: absolute; left: 0; right: 0; bottom: 26px;
    text-align: center; color: var(--paper); font-size: 17px;
  }
  /* Back side */
  .card--back { top: 550px; background: var(--paper); }
  .watermark {
    position: absolute; right: -20px; top: 200px;
    font-weight: 700; font-size: 130px; line-height: 1;
    color: var(--lime-faint); letter-spacing: -2px;
  }
  .card--back .brand {
    position: absolute; left: 0; right: 0; top: 38px;
    text-align: center; font-weight: 700; font-size: 76px;
    color: var(--lime); letter-spacing: -1px; line-height: 1;
  }
  .person { position: absolute; left: 0; right: 0; top: 158px; text-align: center; }
  .person .name { font-weight: 600; font-size: 29px; color: var(--ink); line-height: 1.1; }
  .person .role { font-size: 16px; color: var(--muted); margin-top: 2px; }
  .contacts {
    position: absolute; top: 262px; list-style: none;
    font-size: 16px; color: var(--ink);
  }
  .contacts--left { left: 52px; }
  .contacts--right { left: 372px; top: 252px; font-size: 14px; }
  .contacts li { display: flex; align-items: flex-start; gap: 9px; margin-bottom: 4px; line-height: 20px; }
  .contacts svg { flex: none; margin-top: 2px; }
  .divider {
    position: absolute; left: 348px; top: 250px; width: 1px; height: 72px;
    background: #c9cdd0;
  }
  .tagline {
    position: absolute; left: 0; right: 0; bottom: 0; height: 44px;
    background: var(--slate); color: var(--paper);
    font-size: 16px; text-align: center; line-height: 44px;
  }
</style>
</head>
<body>
<main class="sheet">

  <section class="card card--front" aria-label="Business card front">
    <div class="brand">vorapo</div>
    <div class="site">www.vorapo.com</div>
  </section>

  <section class="card card--back" aria-label="Business card back">
    <div class="watermark" aria-hidden="true">vorapo</div>
    <div class="brand">vorapo</div>

    <div class="person">
      <div class="name">Mara Lin Ellis</div>
      <div class="role">General Manager</div>
    </div>

    <ul class="contacts contacts--left">
      <li>
        <svg width="18" height="18" viewBox="0 0 18 18" aria-hidden="true"><rect width="18" height="18" rx="2" fill="var(--slate-dark)"/><rect x="6" y="3" width="6" height="12" rx="1" fill="none" stroke="#fff" stroke-width="1.4"/></svg>
        08 555 0142
      </li>
      <li>
        <svg width="18" height="18" viewBox="0 0 18 18" aria-hidden="true"><rect width="18" height="18" rx="2" fill="var(--slate-dark)"/><path d="M4 7c0-2 10-2 10 0v1h-3V7H7v1H4z" fill="#fff"/><rect x="5" y="9" width="8" height="5" rx="1" fill="#fff"/></svg>
        01 555 0178
      </li>
      <li>
        <svg width="18" height="18" viewBox="0 0 18 18" aria-hidden="true"><rect width="18" height="18" rx="2" fill="var(--slate-dark)"/><rect x="3.5" y="5" width="11" height="8" fill="none" stroke="#fff" stroke-width="1.3"/><path d="M3.5 5l5.5 4.5L14.5 5" fill="none" stroke="#fff" stroke-width="1.3"/></svg>
        information@vorapo.com
      </li>
    </ul>

    <div class="divider" aria-hidden="true"></div>

    <ul class="contacts contacts--right">
      <li style="font-size:16px">
        <svg width="18" height="18" viewBox="0 0 18 18" aria-hidden="true"><rect width="18" height="18" rx="2" fill="var(--slate-dark)"/><circle cx="9" cy="9" r="5" fill="none" stroke="#fff" stroke-width="1.2"/><path d="M4 9h10M9 4c-2.5 3-2.5 7 0 10M9 4c2.5 3 2.5 7 0 10" fill="none" stroke="#fff" stroke-width="1"/></svg>
        www.vorapo.com
      </li>
      <li>
        <svg width="18" height="18" viewBox="0 0 18 18" aria-hidden="true"><rect width="18" height="18" rx="2" fill="var(--slate-dark)"/><path d="M4 7c0-2 10-2 10 0v1h-3V7H7v1H4z" fill="#fff"/><rect x="5" y="9" width="8" height="5" rx="1" fill="#fff"/></svg>
        <span>48 Harbor Lane, #20417<br>Fenwick, CA 95012</span>
      </li>
    </ul>

    <div class="tagline">We can add some tagline text here center align</div>
  </section>

</main>
</body>
</html>
```